Amaranth an Quinoa Instant Flour - Packaging Design for Tovira Marketplace

I need a package design for the product that I have to sell on Tovira.

The current design needs to be adjusted to the US market.

Target Market(s)

tovira marketplace

Industry/Entity Type

Alimenticia

Font styles to use
Decorative

Colors
F0912C
F2A743
F7CA91
FBE8D2
FDF5EE

Requirements
Must have
• Design appropriate to the type of market to which it is directed
Nice to have
• A design suitable for Tovira

```html
<!DOCTYPE html>
<html lang="en">
<head>
<meta charset="UTF-8">
<title>Nutrelle Amaranth and Quinoa Flour – Pouch Front</title>
<link href="https://fonts.googleapis.com/css2?family=Titan+One&display=swap" rel="stylesheet">
<style>
  :root {
    --page: #ffffff;
    --band: #dd8426;
    --band-dark: #c9651c;
    --sun-light: #fde873;
    --sun: #f6b81e;
    --sun-deep: #f0912c;
    --swoosh: #fbe8a0;
    --ink-blue: #1e3a8e;
    --brand-red: #c62a22;
    --badge-red: #d83a2c;
    --cream: #fdf5ee;
    --milk: #ffffff;
  }
  * { margin: 0; padding: 0; box-sizing: border-box; }
  html, body {
    width: 894px; height: 1200px; overflow: hidden;
    background: var(--page);
  }
  .canvas { position: relative; width: 894px; height: 1200px; }
  .pouch-front {
    position: absolute; left: 103px; top: 120px;
    width: 682px; height: 911px; display: block;
  }
  .pouch-front text { font-family: "Titan One", "Arial Rounded MT Bold", sans-serif; }
  .title-line {
    fill: var(--ink-blue);
    stroke: var(--milk); stroke-width: 9px; paint-order: stroke fill;
    stroke-linejoin: round;
  }
  .brand-name { fill: var(--brand-red); }
  .seal-text { fill: var(--ink-blue); }
  .seal-milk { fill: var(--milk); stroke: var(--ink-blue); stroke-width: 3px; paint-order: stroke fill; }
  .vitamin-letter { fill: var(--sun-deep); }
  .weight-text { fill: var(--milk); }
</style>
</head>
<body>
<main class="canvas">
  <svg class="pouch-front" viewBox="0 0 824 1100" xmlns="http://www.w3.org/2000/svg" aria-label="Nutrelle Amaranth and Quinoa flour pouch front">
    <defs>
      <radialGradient id="sunGlow" cx="0.5" cy="0.42" r="0.7">
        <stop offset="0" stop-color="var(--sun-light)"/>
        <stop offset="0.55" stop-color="var(--sun)"/>
        <stop offset="1" stop-color="var(--sun-deep)"/>
      </radialGradient>
      <linearGradient id="lowerSweep" x1="0" y1="0" x2="0" y2="1">
        <stop offset="0" stop-color="var(--sun-deep)"/>
        <stop offset="1" stop-color="var(--band-dark)"/>
      </linearGradient>
      <linearGradient id="drinkFill" x1="0" y1="0" x2="0" y2="1">
        <stop offset="0" stop-color="#6b4330"/>
        <stop offset="0.35" stop-color="#c79a7c"/>
        <stop offset="1" stop-color="#a8704f"/>
      </linearGradient>
    </defs>

    <!-- background -->
    <rect class="pouch-body" width="824" height="1100" fill="url(#sunGlow)"/>

    <!-- swooshes -->
    <path class="swoosh-upper" d="M0 260 C 120 120, 300 55, 470 45 L 560 45 C 380 70, 160 150, 0 330 Z" fill="var(--swoosh)" opacity="0.8"/>
    <path class="swoosh-right" d="M824 430 C 800 640, 700 790, 560 880 L 600 880 C 740 800, 820 660, 824 560 Z" fill="var(--swoosh)" opacity="0.75"/>

    <!-- lower sweep -->
    <path class="sweep-lower" d="M0 890 C 200 980, 560 960, 824 770 L 824 1100 L 0 1100 Z" fill="url(#lowerSweep)"/>
    <path class="sweep-lower-edge" d="M0 870 C 200 960, 560 945, 824 750 L 824 775 C 560 965, 200 985, 0 900 Z" fill="var(--swoosh)"/>

    <!-- seal bands -->
    <rect class="seal-band-top" x="0" y="0" width="824" height="45" fill="var(--band)"/>
    <rect class="seal-band-bottom" x="0" y="1058" width="824" height="42" fill="var(--band-dark)" opacity="0.85"/>

    <!-- brand -->
    <text class="brand-name" x="425" y="194" font-size="54" text-anchor="middle">Nutrelle</text>

    <!-- drink mascot illustration -->
    <path class="drink-illustration" role="img" aria-label="Illustration of a smiling chocolate milk glass with straw and splash"
      d="M40 500 C 120 475, 360 475, 435 500 L 400 955 L 120 955 Z" fill="url(#drinkFill)" opacity="0.9"/>

    <!-- product title -->
    <g class="product-title">
      <text class="title-line" x="122" y="388" font-size="82" textLength="392" lengthAdjust="spacingAndGlyphs" transform="rotate(-6 122 388)">Amaranth</text>
      <text class="title-line" x="545" y="338" font-size="52" textLength="108" lengthAdjust="spacingAndGlyphs" transform="rotate(-6 545 338)">and</text>
      <text class="title-line" x="285" y="428" font-size="78" textLength="262" lengthAdjust="spacingAndGlyphs" transform="rotate(-6 285 428)">Quinoa</text>
      <text class="title-line" x="568" y="404" font-size="62" textLength="162" lengthAdjust="spacingAndGlyphs" transform="rotate(-6 568 404)">flour</text>
    </g>

    <!-- milk powder seal -->
    <g class="milk-seal">
      <circle cx="555" cy="580" r="98" fill="var(--milk)"/>
      <circle cx="555" cy="580" r="70" fill="var(--sun)"/>
      <text class="seal-text" x="553" y="548" font-size="24" text-anchor="middle">with</text>
      <text class="seal-milk" x="555" y="590" font-size="40" text-anchor="middle">Milk</text>
      <text class="seal-text" x="550" y="627" font-size="24" text-anchor="middle">powder</text>
    </g>

    <!-- ingredient icons -->
    <circle class="cocoa-icon" role="img" aria-label="Cocoa pod icon" cx="762" cy="530" r="26" fill="var(--cream)"/>
    <rect class="grain-icon" role="img" aria-label="Amaranth stalk icon" x="690" y="600" width="46" height="150" rx="23" fill="var(--swoosh)" transform="rotate(35 713 675)"/>

    <!-- vitamins -->
    <g class="vitamins">
      <circle cx="596" cy="788" r="14" fill="var(--cream)"/>
      <text class="vitamin-letter" x="596" y="793" font-size="12" text-anchor="middle">BE</text>
      <circle cx="636" cy="772" r="14" fill="var(--cream)"/>
      <text class="vitamin-letter" x="636" y="778" font-size="16" text-anchor="middle">B</text>
      <circle cx="624" cy="818" r="14" fill="var(--cream)"/>
      <text class="vitamin-letter" x="624" y="824" font-size="16" text-anchor="middle">C</text>
    </g>

    <!-- net weight -->
    <g class="net-weight">
      <rect x="447" y="953" width="273" height="48" rx="10" fill="var(--badge-red)"/>
      <text class="weight-text" x="583" y="986" font-size="24" text-anchor="middle" textLength="236" lengthAdjust="spacingAndGlyphs">Met Weigth 200 g</text>
    </g>
  </svg>
</main>
</body>
</html>
```